Lumen Botanicals Label Project- Updates made to project!

Project Scope: Branding opportunity for internet based skin care line. Design coordinating label for 4 different products. Each design shall be editable in Adobe Illustrator as a template including all fonts, symbols, and guides. Submit a design for all 4 products (preferably together as it would look on a retail shelf), business card, and logo.
Cleanser: STEP 1 Label Size: 5 x 4.5 inches (w x h) CALM CLEANSER
Toner: STEP 2 Label Size: 5 x 4.5 inches (w x h) TRANQUIL TONER- A piece of each crystal sits at the bottom of each solution. It coordinates with the "Quiet Heart" of our logo.
Serum STEP 3 Label Size: Label Size: 4.25 x 2.25 ANTI-AGING SERUM
Moisturizer: STEP 4 Label Size: Label Size: 1”x7.25” MOISTURIZER
Each label needs to include:
Front:
Attractive larger sized STEP #
Logo
Product name and short description
Decorative design Symbol(s)
Back:
Area on back to say short description
Directions for use
Larger area for ingredients
Website: www.lumenbotanicals-example.com
Address of distribution
Barcode

Lumen Skin Care, an esthetician created line provides organic and natural based products for all skin types. With an emphasis on anti-aging, this simple 4- step system can be used by many including pregnant and oncology consumers. The unique thing about our line is that the toners and serums contain crystals such as amethyst and rose quarts to promote Quiet Heart as well as Bright Face. Each product is handmade with natural, quality ingredients and are 70-90% Organic.
Target Market: Women ages 30-45 years old. This demographic is on the go, and wants a simple-easy to read label, & a skin care system that addresses her concerns. Just as this consumer is mindful of her fitness and what she puts in her body, she tends to purchase environmentally friendly, and natural products. Health and wellness trends reflect this, as organic beauty products are expected to grow 74% from 2013 to 2018. She enjoys meditation and yoga, and she is curious about eastern medicine holistic healing trends.

Company Name: Lumen Skin Care
Tagline: Quiet Heart- Bright Face
Package Feel: Simple, elegant easy to read step on each product. STEP 1: AM/PM. Attractive numbering. A symbol that reflects the brand. Not necessarily a Lumen or Crystal because the name speaks for itself. Beautiful, soft, eye catching design that draws the consumer to pick it up. Clear or white label welcomed. Some color palettes provided.
Descriptive words the packaging should represent: Yoga, Zen, mystic, eye catching, healing energy, natural, quality ingredients, sophisticated, beautiful, serenity, easy to read- bold-attractive numbering on front.
Inspiration Brands: VARLA Organics- Beautiful watercolor packaging that resonates a "feeling"

Attached are pictures of the packaging, inspirational pictures, skin care lines that are attractive, ect.

Packaging SPECS:

Cleanser:
Color Clear
Size 4 oz
Material PET
Case Pack
Neck Finish 24-410
Diameter 1.58 in / 4.013 cm
Height 6 in / 15.240 cm
Label Dimensions 5x4.5
Print Dimensions 5x4.5
Print Dimensions in (diameter)

TONER BOTTLE: Same as above

SERUM BOTTLE:
Color Clear
Size 2 oz
Material PET
Neck Finish 20-410
Diameter 1.358 in / 3.449 cm
Height 3.274 in / 8.316 cm

Moisturizer:
2.3 oz
Height:53 mm
Diameter: 60 mm
Neck: 58/400

Target Market(s)

Women ages 30-45 years old. This demographic is on the go, and wants a simple-easy to read label, & a skin care system that addresses her concerns. Just as this consumer is mindful of her fitness and what she puts in her body, she tends to purchase environmentally friendly, and natural products. Health and wellness trends reflect this, as organic beauty products are expected to grow 74% from 2013 to 2018. She enjoys meditation and yoga, and she is curious about eastern medicine holistic healing trends.

Industry/Entity Type

Skin Care Product

Contact Information for Business Card

Details given upon completion.

Logo Text

Lumen Botanicals Quiet Heart- Bright Face

Requirements
Must have
• A large step number on the front. Coordinating symbols and colors. Must have a professional retail look and be easy to read.
Nice to have
• Clean, simple, eye catching packaging. Watercolor designs. Designs that inspire "feelings" www.varlaorganics-example.com

```html
<!DOCTYPE html>
<html lang="en">
<head>
<meta charset="utf-8">
<title>Lumen Skin Care – Label Set</title>
<link rel="stylesheet" href="https://fonts.googleapis.com/css2?family=Josefin+Sans:wght@300&family=Dancing+Script:wght@700&family=Raleway:wght@400;500&family=Open+Sans:wght@400&family=Kaushan+Script&display=swap">
<style>
  :root {
    --paper: #ffffff;
    --blush: #e2d3cf;
    --sand: #d8c6bc;
    --ink: #2e2b2b;
    --grey: #6e6a69;
    --label-edge: #ece6e3;
  }
  * { box-sizing: border-box; margin: 0; padding: 0; }
  html, body { width: 1200px; height: 848px; overflow: hidden; background: var(--paper); }
  .canvas { position: relative; width: 1200px; height: 848px; background: var(--paper); }

  .brand-band {
    position: absolute; left: 148px; top: 0; width: 198px; height: 330px;
    background: var(--blush); border-radius: 0 0 0 0;
  }
  .brand-mandala {
    position: absolute; left: 92px; top: 256px; width: 312px; height: 312px;
  }

  .label {
    position: absolute; bottom: 148px; background: var(--paper);
    border: 1px solid var(--label-edge); overflow: hidden;
    box-shadow: 0 6px 18px rgba(0,0,0,0.06);
  }
  .label-tall { width: 160px; height: 380px; }
  .label-serum { width: 140px; height: 290px; }
  .label-jar { width: 170px; height: 150px; }

  .label-base {
    position: absolute; left: 0; right: 0; bottom: 0; background: var(--sand);
  }
  .label-mark { position: absolute; left: 50%; transform: translateX(-50%); }
  .logo-name {
    position: absolute; left: 0; right: 0; text-align: center;
    font-family: "Josefin Sans", sans-serif; font-weight: 300;
    color: var(--ink); letter-spacing: 2px;
  }
  .tagline {
    position: absolute; left: 0; right: 0; text-align: center;
    font-family: "Dancing Script", cursive; font-weight: 700;
    color: var(--ink); line-height: 1.25;
  }
  .product-name {
    position: absolute; left: 0; right: 0; text-align: center;
    font-family: "Raleway", sans-serif; font-weight: 500; color: var(--grey);
    line-height: 1.05; text-transform: uppercase;
  }
  .product-name .sub { display: block; font-weight: 400; }
  .product-copy {
    position: absolute; left: 12px; right: 12px; text-align: center;
    font-family: "Open Sans", sans-serif; font-size: 8px; line-height: 1.35; color: var(--ink);
  }
  .step-word {
    position: absolute; font-family: "Raleway", sans-serif; color: var(--ink);
    letter-spacing: 1px;
  }
  .step-number {
    position: absolute; font-family: "Kaushan Script", cursive; color: #111; line-height: 1;
  }
</style>
</head>
<body>
<main class="canvas">

  <div class="brand-band"></div>
  <svg class="brand-mandala" viewBox="0 0 312 312" role="img" aria-label="Ornamental lace mandala flower, the brand's decorative symbol">
    <circle cx="156" cy="156" r="156" fill="#f1ebe8"/>
    <circle cx="156" cy="156" r="98" fill="var(--blush)"/>
  </svg>

  <!-- Step 1: Cleanser -->
  <section class="label label-tall" style="left:500px;">
    <div class="label-base" style="height:120px;"></div>
    <svg class="label-mark" style="top:16px;" width="54" height="54" viewBox="0 0 54 54" role="img" aria-label="Mandala symbol">
      <circle cx="27" cy="27" r="27" fill="#8a7f7c"/>
    </svg>
    <div class="logo-name" style="top:80px; font-size:30px;">LUMEN</div>
    <div class="tagline" style="top:124px; font-size:15px;">Quiet Heart<br>Bright Face</div>
    <div class="product-name" style="top:178px; font-size:30px; color:#555;">Calm<span class="sub" style="font-size:15px;">Cleanser</span></div>
    <p class="product-copy" style="top:232px;">Lorem ipsum dolor sit amet, consectetuer adipiscing elit, sed diam nonummy nibh.</p>
    <div class="step-number" style="right:30px; bottom:12px; font-size:84px;">1</div>
    <div class="step-word" style="right:10px; bottom:10px; font-size:12px;">STEP:</div>
  </section>

  <!-- Step 2: Toner -->
  <section class="label label-tall" style="left:680px;">
    <div class="label-base" style="height:110px;"></div>
    <svg class="label-mark" style="top:16px;" width="54" height="54" viewBox="0 0 54 54" role="img" aria-label="Mandala symbol">
      <circle cx="27" cy="27" r="27" fill="#8a7f7c"/>
    </svg>
    <div class="logo-name" style="top:80px; font-size:30px;">LUMEN</div>
    <div class="tagline" style="top:124px; font-size:15px;">Quiet Heart<br>Bright Face</div>
    <div class="product-name" style="top:182px; font-size:19px;">Tranquil<span class="sub" style="font-size:14px;">Toner</span></div>
    <p class="product-copy" style="top:226px;">Lorem ipsum dolor sit amet, consectetuer adipiscing elit, sed diam nonummy nibh.</p>
    <div class="step-word" style="left:18px; bottom:30px; font-size:13px;">STEP:</div>
    <div class="step-number" style="right:24px; bottom:14px; font-size:70px;">2</div>
  </section>

  <!-- Step 3: Serum -->
  <section class="label label-serum" style="left:860px;">
    <div class="label-base" style="height:86px;"></div>
    <svg class="label-mark" style="top:14px;" width="44" height="44" viewBox="0 0 44 44" role="img" aria-label="Mandala symbol">
      <circle cx="22" cy="22" r="22" fill="#8a7f7c"/>
    </svg>
    <div class="logo-name" style="top:66px; font-size:25px;">LUMEN</div>
    <div class="tagline" style="top:102px; font-size:12px;">Quiet Heart<br>Bright Face</div>
    <div class="product-name" style="top:146px; font-size:15px;">Anti-Aging<span class="sub" style="font-size:12px;">Serum</span></div>
    <p class="product-copy" style="top:180px; left:8px; right:8px;">Lorem ipsum dolor sit amet, consectetuer adipiscing elit, sed diam nonummy nibh.</p>
    <div class="step-word" style="left:16px; bottom:34px; font-size:12px;">STEP:</div>
    <div class="step-number" style="right:22px; bottom:10px; font-size:60px;">3</div>
  </section>

  <!-- Step 4: Moisturizer -->
  <section class="label label-jar" style="left:1020px;">
    <div class="label-base" style="top:0; bottom:auto; left:0; right:auto; width:58px; height:150px;"></div>
    <div class="step-word" style="left:8px; top:18px; font-size:12px;">STEP:</div>
    <div class="step-number" style="left:12px; top:40px; font-size:54px;">4</div>
    <svg class="label-mark" style="top:14px; left:114px;" width="34" height="34" viewBox="0 0 34 34" role="img" aria-label="Mandala symbol">
      <circle cx="17" cy="17" r="17" fill="#8a7f7c"/>
    </svg>
    <div class="logo-name" style="top:56px; left:62px; font-size:22px;">LUMEN</div>
    <div class="tagline" style="top:84px; left:62px; font-size:9px; font-family:'Open Sans', sans-serif; font-weight:400;">Quiet Heart Bright Face</div>
    <div class="product-name" style="top:102px; left:62px; font-size:13px; color:#aaa;">Moisturizer</div>
  </section>

</main>
</body>
</html>
```